Zerbani Facilities Management brochure

to design suitable company brochure compatible with company scope work, ee are at Zerbani handling all soft services such as housekeeping , landscaping, waste mangement and pest control and hard services such as building renovations and MEP maintenance ,,,,,,,,,,,,................nnnñnnnnnnnnnnnnnnnnnnnnnnnnnnnnnnnnnnnnnnmnñmmmmmmmmmmmmmmmmm

Target Market(s)

Saudi Arabia

Industry/Entity Type

Facilities Management

Font styles to use
Serif

Requirements
Must have
• Thems matching facilities management feild
Nice to have
• Innovation
Should not have
• Strangers faces photos

```html
<!DOCTYPE html>
<html lang="en">
<head>
<meta charset="utf-8">
<title>Zerbani Facilities Management — Brochure</title>
<link href="https://fonts.googleapis.com/css2?family=Oswald:wght@400;500;600;700&family=Roboto:wght@300;400;500;700&display=swap" rel="stylesheet">
<style>
:root{
  --stage:#dcdcdc;
  --paper:#f7f7f7;
  --orange:#e8961b;
  --amber:#f2b322;
  --deep-orange:#d9801a;
  --navy:#1f2a3c;
  --red:#d3261f;
  --ink:#2b2b2b;
  --muted:#6b6b6b;
  --mist:#e6e6e6;
  --white:#ffffff;
}
*{box-sizing:border-box;margin:0;padding:0}
html,body{width:1200px;height:4112px;overflow:hidden;background:var(--stage)}
body{font-family:"Roboto",sans-serif;color:var(--ink)}
.sheet{position:relative;width:1200px;height:822.4px}
.spread{position:absolute;left:100px;top:58px;width:1000px;height:707px;display:flex;box-shadow:0 14px 30px rgba(0,0,0,.18)}
.page{position:relative;width:500px;height:707px;background:var(--paper);overflow:hidden}
.page + .page{box-shadow:inset 12px 0 18px -14px rgba(0,0,0,.25)}
.abs{position:absolute}
.ph{position:absolute}
.bg-svg{position:absolute;left:0;top:0;width:500px;height:707px}
.heading{font-family:"Oswald",sans-serif;font-weight:500;color:var(--navy);line-height:1.05}
.heading.rule::after{content:"";display:block;width:52px;height:2px;background:var(--red);margin-top:8px}
.body-text{font-size:6.3px;line-height:1.55;color:var(--muted)}
.folio{position:absolute;bottom:18px;font-size:7px;font-weight:700;color:var(--white);background:var(--orange);padding:2px 7px}
.folio.left{left:0}.folio.right{right:0}
.footer-line{position:absolute;bottom:26px;height:1px;background:#cfcfcf}
.footer-url{position:absolute;bottom:22px;font-size:5.5px;color:var(--muted)}
.brand{display:flex;align-items:center;gap:6px;font-family:"Oswald",sans-serif;font-weight:500;font-size:20px}
.brand .mark{width:16px;height:16px}
.badge{width:64px;height:34px;border:1.5px solid rgba(255,255,255,.8);border-radius:4px}
.icon{width:30px;height:30px;border-radius:50%;display:flex;align-items:center;justify-content:center}
.icon svg{width:16px;height:16px}
.cap{font-family:"Oswald",sans-serif;font-size:7.5px;letter-spacing:.3px;text-transform:uppercase}
.tiny{font-size:5.5px;line-height:1.5;color:var(--muted)}
.cols{display:grid;gap:14px}
.pill{position:absolute;height:30px;border-radius:15px;background:var(--mist);display:flex;align-items:center;padding-left:38px;font-family:"Oswald",sans-serif;font-weight:600;font-size:10.5px;color:var(--navy);letter-spacing:.4px}
.pill .dot{position:absolute;left:8px;top:5px;width:20px;height:20px;border-radius:50%;background:var(--navy)}
.bullets{list-style:none;font-size:7.3px;color:var(--white);line-height:1.5}
.bullets li{position:relative;padding-left:10px;margin-bottom:4px}
.bullets li::before{content:"";position:absolute;left:0;top:4px;width:4px;height:4px;border-radius:50%;background:var(--navy)}
</style>
</head>
<body>

<!-- Cover spread -->
<section class="sheet">
  <div class="spread">
    <div class="page back-cover">
      <div class="ph" role="img" aria-label="Aerial photo of a Saudi city skyline in warm desert light" style="left:0;top:0;width:500px;height:360px;background:linear-gradient(160deg,#b9a58b 0%,#d3b58a 45%,#c69553 100%)"></div>
      <svg class="bg-svg" viewBox="0 0 500 707"><path d="M0 270 Q250 230 500 330 V707 H0 Z" fill="var(--orange)"/><path d="M0 270 Q250 230 500 330" fill="none" stroke="var(--amber)" stroke-width="6" opacity=".7"/></svg>
      <div class="abs brand" style="right:40px;top:34px;color:var(--navy)"><span class="mark" style="background:var(--red)"></span>Zerbani</div>
      <div class="abs badge" style="left:40px;top:300px"></div>
      <div class="abs" style="left:40px;top:350px;color:var(--white)">
        <div style="font-family:'Oswald',sans-serif;font-size:18px;font-weight:600;letter-spacing:1px">CONTACT US</div>
        <div style="font-size:8px;line-height:1.6;margin-top:8px;width:230px">Head Office: 14 Palm Grove Road,<br>Al Noor District, Riyadh 12345,<br>Kingdom of Saudi Arabia</div>
        <div style="font-size:8px;line-height:1.9;margin-top:14px">
          <div>T: +966 11 000 1234</div>
          <div>E: info@zerbani-fm.com</div>
          <div>W: www.zerbani-fm.com</div>
        </div>
      </div>
    </div>
    <div class="page front-cover">
      <div class="ph" role="img" aria-label="Photo of a golden timber roof structure" style="left:180px;top:0;width:320px;height:330px;background:linear-gradient(135deg,#f3d28a 0%,#d9a24c 55%,#b97a2a 100%)"></div>
      <svg class="bg-svg" viewBox="0 0 500 707"><path d="M0 420 Q260 360 500 300 V707 H0 Z" fill="var(--orange)"/><path d="M0 420 Q260 360 500 300" fill="none" stroke="var(--amber)" stroke-width="6" opacity=".7"/></svg>
      <div class="abs brand" style="right:40px;top:372px;color:var(--white)"><span class="mark" style="background:var(--white)"></span>Zerbani</div>
      <div class="abs badge" style="left:30px;top:480px"></div>
      <div class="abs" style="right:40px;top:450px;text-align:right;color:var(--white);font-family:'Oswald',sans-serif;line-height:1">
        <div style="font-size:26px;font-weight:400">Your</div>
        <div style="font-size:30px;font-weight:400">Success</div>
        <div style="font-size:30px;font-weight:700;margin-top:4px">IS OUR PRIMARY</div>
        <div style="font-size:36px;font-weight:700">GOAL</div>
        <div style="font-family:'Roboto',sans-serif;font-size:9px;font-weight:500;margin-top:14px">www.zerbani-fm.com</div>
      </div>
    </div>
    <div class="ph" role="img" aria-label="Circular photo of a modern blue and purple office building" style="left:290px;top:60px;width:420px;height:420px;border-radius:50%;border:6px solid var(--white);background:linear-gradient(150deg,#6fa3d8 0%,#2a57a3 45%,#4a2d57 100%)"></div>
  </div>
</section>

<!-- Director & leadership spread -->
<section class="sheet">
  <div class="spread">
    <div class="page">
      <svg class="bg-svg" viewBox="0 0 500 707"><path d="M120 0 H500 V200 Q380 300 200 250 Q140 230 120 160 Z" fill="var(--orange)"/></svg>
      <div class="abs" style="left:200px;top:26px;width:270px">
        <div class="heading" style="font-size:17px;color:#8e1b16;font-style:italic">Message From Managing Director</div>
        <p style="font-size:6.5px;line-height:1.6;color:var(--white);margin-top:8px">It gives me great pleasure to welcome you to Zerbani. For many years we have grown with our clients, building trust through quality, safety and care across every facility we serve in the Kingdom.</p>
      </div>
      <div class="ph" role="img" aria-label="Portrait photo of the managing director at his desk" style="left:95px;top:140px;width:190px;height:190px;border-radius:50%;border:5px solid var(--white);background:linear-gradient(160deg,#c9c2b8,#7f7468)"></div>
      <div class="abs cols body-text" style="left:38px;top:360px;width:430px;grid-template-columns:repeat(3,1fr)">
        <p>Today, change is everywhere. Our customers expect reliable, modern and cost effective service, and we respond with skilled people, proven methods and a clear focus on results for every building we manage.</p>
        <p>Zerbani Services Company has built a strong record in housekeeping, landscaping, waste management and pest control, alongside renovation and MEP maintenance for large sites.</p>
        <p>We remain committed to our teams, our partners and the communities we serve, and we look forward to a future of shared growth, innovation and lasting value.</p>
      </div>
      <div class="footer-line" style="left:40px;width:420px"></div>
      <div class="folio left">01</div>
    </div>
    <div class="page">
      <svg class="bg-svg" viewBox="0 0 500 707"><circle cx="300" cy="600" r="430" fill="var(--orange)"/></svg>
      <div class="abs heading rule" style="left:150px;top:48px;font-size:28px">Our Leadership Team</div>
      <div class="abs" style="left:110px;top:170px;width:300px;color:var(--white);font-size:8px;line-height:1.6;font-weight:500">
        <span style="font-family:'Oswald',sans-serif;font-size:22px;color:#8e1b16;line-height:0">&ldquo;</span> We strongly believe in long-term partnerships with a clear roadmap of how we add value to our clients, our people and the wider community through excellence and trust. <span style="font-family:'Oswald',sans-serif;font-size:22px;color:#8e1b16;line-height:0">&rdquo;</span>
      </div>
      <div class="ph" role="img" aria-label="Flat illustration of a team steering a paper boat together" style="left:40px;top:300px;width:430px;height:330px;border-radius:8px;background:linear-gradient(180deg,rgba(255,214,140,.55),rgba(242,179,34,.85))"></div>
      <div class="folio right">02</div>
    </div>
  </div>
</section>

<!-- Objective & footprint spread -->
<section class="sheet">
  <div class="spread">
    <div class="page">
      <div class="abs heading rule" style="left:40px;top:50px;font-size:22px">Business Objective</div>
      <div class="abs" style="left:40px;top:100px;font-size:7.5px;font-weight:700;color:var(--navy)">MARKET TRENDSETTER IN THE INDUSTRIAL SERVICES MANAGEMENT DOMAIN.</div>
      <div class="abs" style="left:40px;top:145px;display:flex;gap:40px">
        <div style="width:110px">
          <div class="icon" style="background:var(--navy)"><svg viewBox="0 0 16 16"><path d="M2 13 L7 5 L10 9 L12 7 L15 13 Z" fill="#fff"/></svg></div>
          <div class="cap" style="color:var(--orange);margin-top:12px">Mission</div>
          <p class="tiny">To deliver best in class services to our clients and partners across the Kingdom.</p>
        </div>
        <div style="width:110px">
          <div class="icon" style="background:var(--red)"><svg viewBox="0 0 16 16"><ellipse cx="8" cy="8" rx="7" ry="4" fill="#fff"/><circle cx="8" cy="8" r="2" fill="var(--red)"/></svg></div>
          <div class="cap" style="color:var(--orange);margin-top:12px">Vision</div>
          <p class="tiny">To be the market trendsetter in services management, raising the highest standards.</p>
        </div>
        <div style="width:110px">
          <div class="icon" style="background:var(--mist)"><svg viewBox="0 0 16 16"><path d="M2 10 H7 L10 8 L14 10 L10 13 H2 Z" fill="var(--muted)"/><circle cx="9" cy="5" r="2.5" fill="var(--muted)"/></svg></div>
          <div class="cap" style="color:var(--orange);margin-top:12px">Value</div>
          <p class="tiny">We believe in value driven service, quality and safety for every site we support.</p>
        </div>
      </div>
      <div class="ph" role="img" aria-label="Photo of a bright modern office lobby with glass walls and polished floor" style="left:0;top:300px;width:500px;height:407px;border-radius:250px 250px 0 0/90px 90px 0 0;background:linear-gradient(170deg,#b9b08e 0%,#8a6a3f 55%,#5a3f24 100%)"></div>
      <div class="folio left">03</div>
    </div>
    <div class="page">
      <div class="abs heading rule" style="left:38px;top:36px;font-size:20px">Zerbani :<br>Solutions Inspired</div>
      <div class="abs cols body-text" style="left:38px;top:106px;width:424px;grid-template-columns:1fr 1fr">
        <p>ZERBANI offers a comprehensive range of smart, innovative facilities management solutions that target cost effective, sustainable results at our clients' facilities and workplaces, including technical solutions and soft services.</p>
        <p>Solutions and specialised services are delivered across a variety of sectors and clients. At Zerbani we combine a large pool of trained resources with industry expertise to meet diverse business needs.</p>
      </div>
      <svg class="bg-svg" viewBox="0 0 500 707"><path d="M0 175 Q250 215 500 175 V390 Q250 470 0 390 Z" fill="var(--mist)"/></svg>
      <div class="abs" style="left:0;top:200px;width:500px;text-align:center;font-family:'Oswald',sans-serif;font-weight:600;font-size:19px;color:var(--navy)">OUR FOOTPRINT*</div>
      <div class="abs" style="left:30px;top:255px;width:440px;display:flex;justify-content:space-between;text-align:center">
        <div style="width:90px;display:flex;flex-direction:column;align-items:center"><div class="icon" style="background:var(--red)"><svg viewBox="0 0 16 16"><circle cx="8" cy="6" r="4" fill="#fff"/><path d="M5 9 L4 15 L8 13 L12 15 L11 9Z" fill="#fff"/></svg></div><div class="cap" style="color:var(--orange);margin-top:14px">Over 75 years of expertise</div></div>
        <div style="width:90px;display:flex;flex-direction:column;align-items:center;margin-top:14px"><div class="icon" style="background:var(--navy)"><svg viewBox="0 0 16 16"><circle cx="5" cy="5" r="2" fill="#fff"/><circle cx="11" cy="5" r="2" fill="#fff"/><rect x="3" y="8" width="4" height="6" rx="1" fill="#fff"/><rect x="9" y="8" width="4" height="6" rx="1" fill="#fff"/></svg></div><div class="cap" style="color:var(--orange);margin-top:14px">4000+ employees</div></div>
        <div style="width:90px;display:flex;flex-direction:column;align-items:center"><div class="icon" style="background:var(--red)"><svg viewBox="0 0 16 16"><path d="M8 1 C4 1 3 4 3 6 C3 9 8 15 8 15 C8 15 13 9 13 6 C13 4 12 1 8 1Z" fill="#fff"/><circle cx="8" cy="6" r="2" fill="var(--red)"/></svg></div><div class="cap" style="color:var(--orange);margin-top:14px">20+ client locations / sites</div></div>
        <div style="width:90px;display:flex;flex-direction:column;align-items:center;margin-top:-14px"><div class="icon" style="background:var(--navy)"><svg viewBox="0 0 16 16"><path d="M1 8 L5 5 L8 7 L11 5 L15 8 L10 12 L6 12 Z" fill="#fff"/></svg></div><div class="cap" style="color:var(--orange);margin-top:14px">11+ clients</div></div>
      </div>
      <div class="abs" style="left:42px;top:520px;width:416px;height:44px;border-radius:22px;background:var(--amber);display:flex;align-items:center;gap:14px;padding:0 20px">
        <svg width="20" height="20" viewBox="0 0 16 16"><circle cx="8" cy="6" r="4" fill="none" stroke="#fff" stroke-width="1.3"/><rect x="6" y="11" width="4" height="3" fill="#fff"/></svg>
        <span style="font-size:6.8px;color:var(--white);line-height:1.5">"We seek to add value to our customers by reducing their operational costs, mitigating risks and enabling them to augment their productivity."</span>
      </div>
      <p class="abs body-text" style="left:42px;top:585px;width:416px">We at Zerbani are driven to provide our clients with compelling value based solutions through our services management approach and benchmarking, creating workspaces built on quality, trust and service excellence with ISO 9001:2015 certification.</p>
      <div class="footer-line" style="left:40px;width:400px"></div>
      <div class="folio right">04</div>
    </div>
  </div>
</section>

<!-- Segments & IFM spread -->
<section class="sheet">
  <div class="spread">
    <div class="page">
      <svg class="bg-svg" viewBox="0 0 500 707"><path d="M0 150 L360 330 L0 520 Z" fill="var(--amber)"/></svg>
      <div class="abs heading" style="left:60px;top:40px;font-size:20px;font-style:italic">Business Segments</div>
      <div class="ph" role="img" aria-label="Strip of photos showing hospital, offices, bridges, housing and aircraft" style="left:0;top:90px;width:230px;height:440px;border-radius:0 120px 0 0;background:linear-gradient(180deg,#5ea2a6 0%,#7b8fa6 30%,#b6a884 55%,#4e6a48 75%,#8d9aae 100%)"></div>
      <div class="pill" style="left:210px;top:100px;width:240px"><span class="dot"></span>HEALTHCARE</div>
      <div class="pill" style="left:200px;top:150px;width:240px"><span class="dot"></span>COMMERCIAL</div>
      <div class="pill" style="left:190px;top:200px;width:240px"><span class="dot"></span>INFRASTRUCTURE</div>
      <div class="pill" style="left:180px;top:250px;width:240px"><span class="dot"></span>GOVERNMENT</div>
      <div class="pill" style="left:170px;top:300px;width:240px"><span class="dot"></span>RESIDENTIAL</div>
      <div class="pill" style="left:160px;top:350px;width:240px"><span class="dot"></span>EDUCATION</div>
      <div class="pill" style="left:150px;top:400px;width:240px"><span class="dot"></span>AVIATION</div>
      <div class="pill" style="left:140px;top:450px;width:240px"><span class="dot"></span>OIL &amp; GAS</div>
      <div class="folio left">05</div>
    </div>
    <div class="page">
      <div class="abs heading rule" style="left:70px;top:80px;font-size:24px">Integrated Facility<br>Management</div>
      <p class="abs body-text" style="left:70px;top:160px;width:370px">The Need For Professional Integrated Facility Management Services: a single partner for technical, soft and specialised services brings better control, lower cost and one point of accountability.<br><br>At Zerbani we design systems that improve reliability, extend asset life and keep every site safe, clean and fully operational for the people who use it every day.</p>
      <div class="abs" style="left:70px;top:330px;width:380px;height:260px">
        <div class="abs" style="left:20px;top:0;display:flex;align-items:center;gap:10px"><div class="icon" style="width:44px;height:44px;background:var(--red)"><svg viewBox="0 0 16 16"><circle cx="8" cy="6" r="4" fill="#fff"/><rect x="6" y="11" width="4" height="3" fill="#fff"/></svg></div><span class="cap" style="color:var(--orange);width:80px">Technical Solutions</span></div>
        <div class="abs" style="left:210px;top:50px;display:flex;align-items:center;gap:10px"><div class="icon" style="width:44px;height:44px;background:var(--navy)"><svg viewBox="0 0 16 16"><circle cx="4" cy="8" r="2.5" fill="#fff"/><circle cx="12" cy="8" r="2.5" fill="#fff"/><rect x="5" y="7" width="6" height="2" fill="#fff"/></svg></div><span class="cap" style="color:var(--orange);width:90px">Hygiene &amp; Soft Service Solutions</span></div>
        <div class="abs" style="left:0;top:120px;display:flex;align-items:center;gap:10px"><div class="icon" style="width:44px;height:44px;background:var(--navy)"><svg viewBox="0 0 16 16"><circle cx="4" cy="8" r="2" fill="#fff"/><circle cx="12" cy="4" r="2" fill="#fff"/><circle cx="12" cy="12" r="2" fill="#fff"/><path d="M4 8 L12 4 M4 8 L12 12" stroke="#fff" stroke-width="1.2"/></svg></div><span class="cap" style="color:var(--orange);width:80px">Specialised Service Solution</span></div>
        <div class="abs" style="left:180px;top:180px;display:flex;align-items:center;gap:10px"><div class="icon" style="width:44px;height:44px;background:var(--red)"><svg viewBox="0 0 16 16"><circle cx="5" cy="6" r="2.5" fill="#fff"/><circle cx="11" cy="6" r="2.5" fill="#fff"/><rect x="2" y="10" width="12" height="4" rx="2" fill="#fff"/></svg></div><span class="cap" style="color:var(--orange);width:80px">Projects Support Services</span></div>
      </div>
      <div class="footer-line" style="left:40px;width:400px"></div>
      <div class="footer-url" style="left:40px">www.zerbani-fm.com</div>
      <div class="folio right">06</div>
    </div>
  </div>
</section>

<!-- Service offerings spread -->
<section class="sheet">
  <div class="spread">
    <div class="page">
      <svg class="bg-svg" viewBox="0 0 500 707"><path d="M500 0 H390 Q240 60 250 340 Q260 560 380 707 H500 Z" fill="var(--amber)"/></svg>
      <div class="abs heading rule" style="left:22px;top:26px;font-size:34px">Our<br>Service Offerings</div>
      <div class="ph" role="img" aria-label="Circular photo of maintenance workers renovating a single storey building" style="left:18px;top:160px;width:380px;height:380px;border-radius:50%;background:linear-gradient(180deg,#8fb6d9 0%,#cfd9e0 40%,#b78d6c 65%,#8b8f7a 100%)"></div>
      <div class="footer-line" style="left:40px;width:280px"></div>
      <div class="footer-url" style="left:330px">www.zerbani-fm.com</div>
      <div class="folio left">07</div>
    </div>
    <div class="page" style="background:var(--amber)">
      <div class="abs heading rule" style="left:55px;top:110px;font-size:22px;color:var(--white)">Technical Solutions</div>
      <p class="abs" style="left:55px;top:170px;width:380px;font-size:8px;line-height:1.5;color:var(--white)">We are modernising the facilities and workplaces through innovation and providing valuable services.</p>
      <div class="abs" style="left:55px;top:240px;display:flex;gap:10px;align-items:center">
        <div class="icon" style="width:20px;height:20px;background:var(--red)"><svg viewBox="0 0 16 16" style="width:10px;height:10px"><path d="M9 1 L3 9 H8 L7 15 L13 7 H8 Z" fill="#fff"/></svg></div>
        <div style="font-family:'Oswald',sans-serif;font-size:11px;color:var(--white);line-height:1.2">Electro-Mechanical Services<br>&amp; Building Repairs</div>
      </div>
      <div class="abs cols" style="left:55px;top:290px;width:380px;grid-template-columns:1fr 1fr;font-size:5.8px;line-height:1.55;color:var(--white)">
        <p>From capital asset and facility maintenance to managing MEP services and building fabric, our highly trained maintenance professionals take care of the day to day jobs that keep facilities and assets performing optimally. These include:</p>
        <p>Our zero tolerance for unplanned downtime is backed by our reliability maintenance programme and our computer aided facility management system for anticipating and handling equipment failure that could otherwise lead to productivity loss.</p>
      </div>
      <div class="abs cols" style="left:55px;top:390px;width:380px;grid-template-columns:1fr 1fr">
        <ul class="bullets">
          <li>Building Construction</li>
          <li>Building and community housing maintenance</li>
          <li>HVAC Operations and Maintenance</li>
        </ul>
        <ul class="bullets">
          <li>Electrical Operations and Maintenance</li>
          <li>STP / WTP Maintenance</li>
          <li>Building renovation and Maintenance</li>
          <li>Water proofing</li>
        </ul>
      </div>
      <div class="footer-line" style="left:40px;width:400px;background:rgba(255,255,255,.6)"></div>
      <div class="footer-url" style="left:40px;color:var(--white)">www.zerbani-fm.com</div>
      <div class="folio right" style="background:var(--deep-orange)">08</div>
    </div>
  </div>
</section>

</body>
</html>
```